Splash Screen for a new release of software

Our company Tandrel Northfield Group writes business management software for the automotive industry. Early next year we are planning on releasing our new version of Halvorstep, this is a fourth generation product. Our thoughts are to brand this version simply Halvorstep 4, however we do wish to add a certain exclusivity to product hence the addition of Lantern Edition as a signature to the Halvorstep brand. The splash screen has to make the user feel that they are using an upmarket product and are excited to be doing so. I have uploaded an "in house" design for reference purposes, also included our sphere company logo.

```html
<!DOCTYPE html>
<html lang="en">
<head>
<meta charset="utf-8">
<title>Halvorstep 4 – Lantern Edition Splash Screen</title>
<link rel="stylesheet" href="https://fonts.googleapis.com/css2?family=Mulish:wght@400;500;800&display=swap">
<style>
  :root {
    --page-bg: #ffffff;
    --purple-deep: #5e0060;
    --purple-mid: #7a0380;
    --purple-bright: #96009c;
    --magenta-glow: #ff2ee8;
    --disc-fill: #262b30;
    --text-light: #ffffff;
    --text-soft: #f0e6ef;
    --brand-disc: #14070f;
  }
  * { margin: 0; padding: 0; box-sizing: border-box; }
  html, body {
    width: 1200px; height: 1200px; overflow: hidden;
    background: var(--page-bg);
  }
  .canvas { position: relative; width: 1200px; height: 1200px; }
  .splash-card {
    position: absolute; left: 135px; top: 360px;
    width: 957px; height: 517px; border-radius: 22px; overflow: hidden;
    background:
      radial-gradient(ellipse 420px 300px at 50% 45%, var(--purple-bright) 0%, var(--purple-mid) 55%, transparent 100%),
      linear-gradient(90deg, var(--purple-mid) 0%, var(--purple-deep) 20%, var(--purple-mid) 50%, var(--purple-deep) 82%, var(--purple-deep) 100%);
  }
  .light-art { position: absolute; left: 0; top: 0; width: 1200px; height: 1200px; }
  .product-name {
    position: absolute; left: 0; width: 1200px; top: 585px;
    text-align: center; font-family: "Mulish", sans-serif; font-weight: 400;
    font-size: 36px; line-height: 44px; letter-spacing: 1px; color: var(--text-light);
  }
  .edition-name {
    position: absolute; left: 0; width: 1200px; top: 640px;
    text-align: center; font-family: "Mulish", sans-serif; font-weight: 500;
    font-size: 13.5px; letter-spacing: 3px; color: var(--text-soft);
  }
  .release-date {
    position: absolute; left: 173px; top: 834px;
    font-family: "Mulish", sans-serif; font-weight: 500;
    font-size: 14px; letter-spacing: 2.6px; color: var(--text-soft);
  }
  .footer-note {
    position: absolute; left: 0; width: 1202px; top: 835px; text-align: center;
    font-family: "Mulish", sans-serif; font-weight: 500;
    font-size: 13.5px; color: var(--text-light);
  }
  .company-mark {
    position: absolute; left: 934px; top: 401px; width: 122px; height: 122px;
    border-radius: 50%; background: var(--brand-disc);
    display: flex; align-items: center; justify-content: center; text-align: center;
    font-family: "Mulish", sans-serif; font-weight: 800; font-size: 11px;
    line-height: 1.25; letter-spacing: 0.4px; color: var(--text-light);
    padding: 0 14px;
  }
</style>
</head>
<body>
<main class="canvas">
  <section class="splash-card" aria-label="Halvorstep 4 Lantern Edition splash screen"></section>

  <svg class="light-art" viewBox="0 0 1200 1200" aria-hidden="true">
    <defs>
      <radialGradient id="flare-band" cx="0.5" cy="0.5" r="0.5">
        <stop offset="0" stop-color="var(--magenta-glow)" stop-opacity="0.95"/>
        <stop offset="0.6" stop-color="var(--magenta-glow)" stop-opacity="0.35"/>
        <stop offset="1" stop-color="var(--magenta-glow)" stop-opacity="0"/>
      </radialGradient>
      <radialGradient id="soft-glow" cx="0.5" cy="0.5" r="0.5">
        <stop offset="0.7" stop-color="var(--magenta-glow)" stop-opacity="0.8"/>
        <stop offset="1" stop-color="var(--magenta-glow)" stop-opacity="0"/>
      </radialGradient>
    </defs>
    <circle cx="600" cy="617" r="190" fill="url(#soft-glow)"/>
    <ellipse cx="600" cy="617" rx="340" ry="16" fill="url(#flare-band)"/>
    <circle cx="600" cy="617" r="173" fill="var(--disc-fill)"/>
  </svg>

  <h1 class="product-name">HALVORSTEP 4</h1>
  <p class="edition-name">LANTERN EDITION</p>

  <div class="company-mark">Tandrel Northfield Group</div>

  <p class="release-date">JANUARY 21 2025</p>
  <p class="footer-note">Lorem ipsumrem</p>
</main>
</body>
</html>
```